Escape Room Flyer Design - Start up. A5

Flyer is for letterbox drops to get interest and let people know that our business exists and to a lesser extent what an escape room is. We have 1 room (the miller's shadows) and a second room coming soon (Varuna's Vault). I have attached our logo and 2 flyers that I have seen in the past that I really like the design of.
Whether you are having a night out with friends or family, celebrating a special event, planning a team-building activity, or simply wanting a diversion from the doldrums of your workweek, The Lock Box will provide you an unforgettable live-action gaming experience.

Target Market(s)

18-25

Industry/Entity Type

Entertainment

Requirements
Must have
• Logo. Phone number 0417 265 839. Website. www.thelockboxhartwell.com
Bookings essential.
Nice to have
• Mystery, a little bit on the darker side than bright colourful and blocky.
"Many Will Enter…Few Will Escape" tag line
60 minute game. Team work. 2-6 players. All ages.
Should not have
• Cartoons, characters, people

```html
<!DOCTYPE html>
<html lang="en">
<head>
<meta charset="utf-8">
<title>The Lock Box – Escape Room Flyer</title>
<link href="https://fonts.googleapis.com/css2?family=Montserrat:wght@500;600;700;800&display=swap" rel="stylesheet">
<style>
  :root {
    --ink: #1b1b1b;
    --night: #1e1e1e;
    --paper: #ffffff;
    --copper-dark: #c8813f;
    --copper-light: #f8bd6c;
    --copper-dot: #d98a3d;
    --slate: #3d3d3d;
    --grey: #7a7a7a;
    --rule: #9a9a9a;
  }
  * { box-sizing: border-box; margin: 0; padding: 0; }
  html, body { width: 869px; height: 1200px; overflow: hidden; background: var(--paper); }
  body { font-family: "Montserrat", Arial, sans-serif; color: var(--ink); }

  .flyer { position: relative; width: 869px; height: 1200px; overflow: hidden; background: var(--night); }
  .flyer__shapes { position: absolute; inset: 0; }

  .damask { position: absolute; inset: 0; background: radial-gradient(ellipse at 50% 40%, #262626 0%, #1a1a1a 80%); }

  .headline {
    position: absolute; left: 0; top: 28px; width: 869px; text-align: center;
    color: var(--paper); font-weight: 800; font-size: 92px; line-height: 1; letter-spacing: -1px;
  }
  .tagline {
    position: absolute; left: 0; top: 142px; width: 869px; text-align: center;
    color: var(--paper); font-weight: 700; font-size: 33px; line-height: 1;
  }

  .brand {
    position: absolute; left: 251px; top: 712px; width: 366px; text-align: center;
    color: var(--copper-light); font-weight: 800; font-size: 34px; line-height: 1.05; letter-spacing: 1px;
  }

  .features { position: absolute; left: 33px; top: 907px; list-style: none; }
  .features li {
    position: relative; padding-left: 20px; font-size: 13px; font-weight: 600; line-height: 21.5px;
  }
  .features li::before {
    content: ""; position: absolute; left: 0; top: 4px; width: 13px; height: 13px; border-radius: 50%;
    background: linear-gradient(135deg, var(--copper-dark), var(--copper-light));
  }

  .intro {
    position: absolute; left: 34px; top: 1000px; width: 205px;
    font-size: 12.4px; line-height: 17px; text-align: justify; font-weight: 500; hyphens: auto;
  }

  .rooms { position: absolute; right: 46px; top: 870px; width: 260px; text-align: right; }
  .rooms__label { color: var(--grey); font-weight: 800; font-size: 22px; line-height: 23px; }
  .rooms__name { font-weight: 700; font-size: 16px; line-height: 20px; margin-top: 4px; }
  .rooms__rule { height: 3px; background: var(--rule); width: 216px; margin: 9px 0 0 auto; }
  .rooms__label--next { margin-top: 10px; }

  .contact-pill {
    position: absolute; right: 0; top: 1052px; width: 258px; height: 47px;
    background: var(--slate); border-radius: 24px 0 0 24px;
    color: var(--paper); font-size: 23px; font-weight: 600; line-height: 47px; text-align: center; padding-left: 6px;
  }

  .phone {
    position: absolute; left: 620px; top: 1112px;
    display: flex; align-items: center; gap: 8px;
    font-size: 21px; font-weight: 700;
  }
  .phone svg { width: 34px; height: 34px; }

  .web-tab {
    position: absolute; right: 0; top: 1158px; width: 305px; height: 42px;
    background: #0d0d0d; border-radius: 22px 0 0 0;
    color: var(--paper); font-size: 15px; font-weight: 700; line-height: 42px; text-align: center; padding-left: 12px;
  }

  .seal-text {
    position: absolute; left: 298px; top: 990px; width: 272px; text-align: center;
    color: var(--paper); font-weight: 800; font-size: 24px; line-height: 35px;
  }
</style>
</head>
<body>
<main class="flyer">
  <div class="damask" role="img" aria-label="Dark damask wallpaper pattern in black tones"></div>

  <svg class="flyer__shapes" viewBox="0 0 799 1131" preserveAspectRatio="none" aria-hidden="true">
    <defs>
      <linearGradient id="copper-v" x1="0" y1="0" x2="0" y2="1">
        <stop offset="0" stop-color="#c8813f"/>
        <stop offset="1" stop-color="#f8bd6c"/>
      </linearGradient>
      <linearGradient id="copper-h" x1="0" y1="0" x2="1" y2="0">
        <stop offset="0" stop-color="#c8813f"/>
        <stop offset="1" stop-color="#f8bd6c"/>
      </linearGradient>
    </defs>
    <!-- white frame and lower panel -->
    <polygon class="frame" fill="#ffffff"
      points="399,198 598,313 598,500 650,578 650,660 799,740 799,1131 0,1131 0,740 147,660 147,578 200,500 200,313"/>
    <!-- copper chevron -->
    <polygon fill="url(#copper-v)" points="399,274 533,350 533,510 399,435 267,510 267,350"/>
    <!-- dark inner chamber -->
    <polygon fill="#1e1e1e" points="399,501 568,598 568,798 514,830 514,910 287,910 287,830 231,798 231,598"/>
    <!-- seal -->
    <circle cx="399" cy="983" r="136" fill="#ffffff"/>
    <circle cx="399" cy="983" r="125" fill="url(#copper-h)"/>
    <!-- copper footer strip -->
    <rect x="0" y="1120" width="525" height="11" fill="url(#copper-h)"/>
  </svg>

  <h1 class="headline">ESCAPE ROOM</h1>
  <p class="tagline">MANY WILL ENTER...FEW WILL ESCAPE</p>

  <p class="brand">THE<br>LOCK BOX</p>

  <ul class="features">
    <li>60 Minute Game.</li>
    <li>Team Work.</li>
    <li>2-6 Player.</li>
    <li>All Ages.</li>
  </ul>

  <p class="intro">Whether you are having a night out with friends or family, celebrating a special event, planning a team-building activity, or simply wanting a diversion from the doldrums of your workweek, The Lock Box will provide you an unforgettable live-action gaming experience.</p>

  <p class="seal-text">HARTWELL'S<br>FIRST<br>ESCAPE ROOM</p>

  <section class="rooms">
    <p class="rooms__label">WE HAVE<br>1 ROOM</p>
    <p class="rooms__name">THE MILLER'S SHADOWS</p>
    <div class="rooms__rule"></div>
    <p class="rooms__label rooms__label--next">A SECOND ROOM<br>COMING SOON</p>
    <p class="rooms__name">VARUNA'S VAULT</p>
  </section>

  <div class="contact-pill">CONTACT US</div>

  <p class="phone">0417 265 839
    <svg viewBox="0 0 34 34" aria-hidden="true">
      <circle cx="17" cy="17" r="15.5" fill="none" stroke="#1b1b1b" stroke-width="2"/>
      <path d="M12 9.5c1-.8 2-.6 2.5.3l1.4 2.6c.4.8.2 1.5-.5 2l-1 .8c.6 2 2.1 3.8 4 4.8l.9-1c.6-.7 1.3-.8 2-.4l2.5 1.5c.9.5 1 1.5.2 2.4l-1.2 1.3c-1 1-2.6 1.2-4 .5-4-2-7-5.5-8.3-9.8-.4-1.5 0-2.9 1.1-3.8z" fill="#1b1b1b"/>
    </svg>
  </p>

  <div class="web-tab">www.thelockboxhartwell.com</div>
</main>
</body>
</html>
```